Podcast Cover Art for Alliance Horizon Circle

We need a podcast cover design for a podcast called "Alliance Horizon Circle". The podcast is about partnerships in the enterprise software business. The "cover design" is kind of like an album cover and there's a great article here about how to create a stunning Podcast cover art:

https://www.wavelotter.com/blog/10-tips-create-awesome-podcast-artwork

There are also examples in that post linked above.

The Alliance Horizon Circle already has some design themes/elements that I'll attach a background image for reference so you can see the typical colors, fonts, etc.

The cover art should include the words "Alliance Horizon Circle" and include the names of the two artists:

Derek Valtimo
Gordon Pratlund

It should also include the Alliance Horizon Circle logo somewhere. I'll attach that.

I've attached the fonts used for the logo text.

I'll also attach photos of the two artists (2 options to choose from for each). We need your guidance on whether we should include those in some stylized way, or leave them out.

Thanks for the help!

Technical Specifications:

Square Image
3000 x 3000 pixels
Resolution of 72 dpi
PNG or JPEG file types
Colorspace RGB

Colors
0054AA
0677BA
7BADD7
CADEEF
E8F1F8

Requirements
Should not have
• Avoid overused images like microphones and headsets

```html
<!DOCTYPE html>
<html lang="en">
<head>
<meta charset="utf-8">
<title>Alliance Horizon Circle — Podcast Cover</title>
<link href="https://fonts.googleapis.com/css2?family=Archivo+Black&display=swap" rel="stylesheet">
<style>
  :root {
    --band-left: #cfe4f5;
    --band-mid: #b5d8f0;
    --band-right: #6fc5e8;
    --title-blue: #4272bc;
    --title-white: #ffffff;
    --outline-blue: #2f5ea8;
    --shadow-dark: rgba(40, 50, 70, 0.55);
    --glow-teal: rgba(20, 95, 130, 0.55);
    --shirt-light: #e8f1f8;
    --shirt-mid: #a9cde6;
    --shirt-deep: #7badd7;
    --blazer-top: #c9dbe8;
    --blazer-mid: #5d7590;
    --blazer-deep: #23324a;
    --mark-blue: #0054aa;
  }
  * { margin: 0; padding: 0; box-sizing: border-box; }
  html, body { width: 1200px; height: 1200px; overflow: hidden; }
  body { font-family: "Archivo Black", "Arial Black", sans-serif; }

  .cover {
    position: relative;
    width: 1200px;
    height: 1200px;
    overflow: hidden;
    background: linear-gradient(to right,
      var(--band-left) 0 401px,
      var(--band-mid) 401px 802px,
      var(--band-right) 802px 1200px);
  }

  .show-title {
    position: absolute;
    top: 28px;
    left: 0;
    width: 1200px;
    text-align: center;
    font-size: 152px;
    line-height: 126px;
    letter-spacing: -1px;
    text-transform: uppercase;
  }
  .show-title span { display: block; text-shadow: 3px 3px 2px var(--shadow-dark); }
  .show-title .line-blue { color: var(--title-blue); }
  .show-title .line-white { color: var(--title-white); }

  .host-photo {
    position: absolute;
    border-radius: 48% 48% 0 0 / 38% 38% 0 0;
    box-shadow: 0 0 45px 18px var(--glow-teal);
  }
  .host-photo.left {
    left: 40px; top: 490px; width: 620px; height: 760px;
    background: linear-gradient(to bottom,
      var(--shirt-light) 0%, var(--shirt-mid) 55%, var(--shirt-deep) 100%);
  }
  .host-photo.right {
    left: 690px; top: 468px; width: 560px; height: 780px;
    background: linear-gradient(to bottom,
      var(--blazer-top) 0%, var(--blazer-mid) 55%, var(--blazer-deep) 100%);
  }

  .host-name {
    position: absolute;
    top: 1008px;
    font-size: 62px;
    line-height: 70px;
    color: var(--title-white);
    text-transform: uppercase;
    text-shadow:
      -2px -2px 0 var(--outline-blue), 2px -2px 0 var(--outline-blue),
      -2px 2px 0 var(--outline-blue), 2px 2px 0 var(--outline-blue),
      4px 4px 3px var(--shadow-dark);
  }
  .host-name.left { left: 58px; }
  .host-name.right { left: 855px; }

  .brand-mark {
    position: absolute;
    left: 514px;
    top: 980px;
    width: 180px;
    text-align: center;
  }
  .brand-mark svg { display: block; margin: 0 auto 10px; }
  .brand-mark .brand-name {
    display: block;
    font-size: 16px;
    line-height: 20px;
    color: var(--mark-blue);
    text-transform: uppercase;
  }
</style>
</head>
<body>
  <main class="cover">
    <h1 class="show-title">
      <span class="line-blue">Alliance</span>
      <span class="line-white">Horizon</span>
      <span class="line-blue">Circle</span>
    </h1>

    <div class="host-photo left" role="img" aria-label="Portrait photo of host Gordon Pratlund in a light blue shirt"></div>
    <div class="host-photo right" role="img" aria-label="Portrait photo of host Derek Valtimo in a dark blazer"></div>

    <p class="host-name left">Gordon<br>Pratlund</p>
    <p class="host-name right">Derek<br>Valtimo</p>

    <div class="brand-mark">
      <svg width="110" height="110" viewBox="0 0 110 110" aria-hidden="true">
        <circle cx="55" cy="55" r="52" fill="var(--mark-blue)"/>
      </svg>
      <span class="brand-name">Alliance Horizon<br>Circle</span>
    </div>
  </main>
</body>
</html>
```